design my moving truck

We need our moving truck covered- I like the logo you designed-(black background and orange and white) I would like your ideas, I want simple and for it to stand out and get peoples attention as I am driving by
I would like the logo big, MUST HAVE my phone number 318-5276, and MUST HAVE my website address
CorlaDevitt.example
-I would also like it to say BUY or SELL a home with us and use this truck for FREE!
-also for it to say STAGING-PROFESSIONAL VIDEOS-PROFESSIONAL PHOTOS and MORE...
*(WE ARE A REAL ESTATE COMPANY not a moving company, I let my clients use this truck for free)

Target Market(s)

BUYERS AND SELLERS of homes

Industry/Entity Type

Real Estate Agent

Requirements
Must have
• my phone number 555-318-5276
• my website CorlaDevitt.example
• STAGING-PROFESSIONAL PHOTOS-PROFESSIONAL VIDEOS and MORE...

```html
<!DOCTYPE html>
<html lang="en">
<head>
<meta charset="utf-8">
<title>Corla Devitt &amp; Co — Truck Wrap Layout</title>
<link rel="stylesheet" href="https://fonts.googleapis.com/css2?family=Tinos:wght@400;700&family=Arimo:wght@400&display=swap">
<style>
  :root {
    --page-bg: #f1f1f1;
    --page-glow: #ffffff;
    --sky: #b5d7ef;
    --sky-low: #c9e3f3;
    --grass: #5cbf45;
    --grass-dark: #3fae3f;
    --plank: #c49a6b;
    --post: #a87c52;
    --accent: #ff5500;
    --band: #8f1c1f;
    --ink: #111111;
    --white: #ffffff;
    --dim-line: #222222;
  }
  html, body {
    margin: 0;
    padding: 0;
    width: 1200px;
    height: 900px;
    overflow: hidden;
  }
  body {
    background: radial-gradient(ellipse at center, var(--page-glow) 0%, var(--page-bg) 75%);
    font-family: "Tinos", "Times New Roman", serif;
  }
  .wrap-layout {
    position: relative;
    width: 1200px;
    height: 900px;
  }
  .wrap-layout svg {
    position: absolute;
    left: 0;
    top: 0;
  }
  .dim-label {
    font-family: "Arimo", Arial, sans-serif;
    font-size: 16px;
    fill: var(--ink);
  }
  .brand-name {
    font-family: "Tinos", "Times New Roman", serif;
    font-size: 46px;
    font-weight: 400;
    fill: var(--ink);
  }
  .brand-tagline {
    font-family: "Tinos", "Times New Roman", serif;
    font-size: 18px;
    font-weight: 400;
    fill: var(--ink);
  }
  .contact-text {
    font-family: "Tinos", "Times New Roman", serif;
    font-size: 31px;
    fill: var(--ink);
  }
  .services-text {
    font-family: "Tinos", "Times New Roman", serif;
    font-size: 22px;
    font-weight: 700;
    fill: var(--white);
  }
</style>
</head>
<body>
<main class="wrap-layout">
  <svg width="1200" height="900" viewBox="0 0 1200 900" xmlns="http://www.w3.org/2000/svg">
    <defs>
      <linearGradient id="scene-fill" x1="0" y1="250" x2="0" y2="641" gradientUnits="userSpaceOnUse">
        <stop offset="0" stop-color="var(--sky)"/>
        <stop offset="0.78" stop-color="var(--sky-low)"/>
        <stop offset="0.86" stop-color="var(--grass)"/>
        <stop offset="1" stop-color="var(--grass-dark)"/>
      </linearGradient>
    </defs>

    <g class="dimensions" stroke="var(--dim-line)" stroke-width="2">
      <line x1="70" y1="241" x2="1130" y2="241"/>
      <line x1="62" y1="250" x2="62" y2="385"/>
      <line x1="70" y1="393" x2="233" y2="393"/>
      <line x1="1138" y1="250" x2="1138" y2="682"/>
    </g>
    <text class="dim-label" x="597" y="232" text-anchor="middle">?</text>
    <text class="dim-label" x="48" y="324" text-anchor="middle">?</text>
    <text class="dim-label" x="151" y="416" text-anchor="middle">?</text>
    <text class="dim-label" x="1152" y="472" text-anchor="middle">?</text>

    <polygon class="scene" role="img"
      aria-label="Illustrated scene: blue sky with white clouds, a row of red-roofed houses and a green hill"
      points="70,250 1130,250 1130,641 237,641 237,385 70,385"
      fill="url(#scene-fill)"/>

    <rect class="sign-post" x="655" y="428" width="57" height="213" fill="var(--post)"/>
    <rect class="name-panel" x="380" y="330" width="605" height="98" rx="10" fill="var(--plank)"/>
    <text class="brand-name" x="396" y="384" textLength="574" lengthAdjust="spacingAndGlyphs">CORLA DEVITT &amp; CO</text>
    <text class="brand-tagline" x="396" y="415" textLength="576" lengthAdjust="spacing">MONTANA REAL ESTATE BROKERS</text>

    <rect class="web-panel" x="330" y="472" width="325" height="50" rx="6" fill="var(--plank)"/>
    <circle cx="352" cy="495" r="33" fill="var(--plank)"/>
    <g class="globe-icon" fill="none" stroke="var(--accent)" stroke-width="2.5">
      <circle cx="352" cy="495" r="21"/>
      <ellipse cx="352" cy="495" rx="9" ry="21"/>
      <line x1="331" y1="495" x2="373" y2="495"/>
      <line x1="335" y1="484" x2="369" y2="484"/>
      <line x1="335" y1="506" x2="369" y2="506"/>
    </g>
    <text class="contact-text" x="390" y="507" textLength="254" lengthAdjust="spacingAndGlyphs">CorlaDevitt.example</text>

    <rect class="phone-panel" x="712" y="520" width="250" height="50" rx="6" fill="var(--plank)"/>
    <circle cx="955" cy="545" r="33" fill="var(--plank)"/>
    <circle cx="955" cy="545" r="25" fill="var(--white)"/>
    <g class="phone-icon">
      <rect x="945" y="528" width="20" height="34" rx="3" fill="none" stroke="var(--accent)" stroke-width="2.5"/>
      <rect x="948" y="533" width="14" height="22" fill="var(--accent)"/>
      <circle cx="955" cy="558.5" r="1.5" fill="var(--accent)"/>
    </g>
    <text class="contact-text" x="722" y="556" textLength="198" lengthAdjust="spacingAndGlyphs">555-318-5276</text>

    <rect class="services-band" x="237" y="641" width="893" height="41" fill="var(--band)"/>
    <text class="services-text" x="245" y="670" textLength="875" lengthAdjust="spacingAndGlyphs">STAGING-PROFESSIONAL PHOTOS-PROFESSIONAL VIDEOS and MORE...</text>
  </svg>
</main>
</body>
</html>
```